New Website for IT Services Business

We need an uncoded web design for a new company based in Australia called "Falcon IT". We offer specialised point of sale (POS) support to the hospitality industry. We already support hundreds of cafes and restaurants. We are also about to launch and promote a range of new services with the offering of General IT Support being the most important. Other additional services to be offered are Falcon Vault Storage, reselling and supporting Corvel Shieldware and Trelmo Suite.

We have a logo design and our colour scheme is based on the logo with the addition of charcoal grey (see attached logos). We want the pages to reflect precision and efficiency with sharp characteristics. It must be professional but playful/fun elements are encouraged.

Our target audience is restaurant and cafe owners who are interested in finding high quality POS and IT support for their business.

The main call to action on the home page should be either 'Let's Meet For Coffee!' or 'Find out more (by completing a form)'. If you are unsure about what the general text should say then you can use 'Lorem Ipsum' where required.

The site must be viewable at different resolutions and on smart phones and tablets.

The website structure will be quite simple. We require:
- one impressive landing page. Visitors will quickly determine our services and that we provide a very high level of service while also offering value for money. Obviously a clear list of links (however/wherever you like) to the other pages.
- Simple pages with a similar layout for the following:
- Services - "POS & IT Support for the Hospitality Industry" being the main one. With complementary services also listed. Another call to action on this page with the option of 'Let's Meet For Coffee' or a "More information/Pricing" form to be completed by the visitor.
- Products - will be a small online storefront for a few simple products.
- About - Business background. 2x Directors with a photo and brief Bio.
- Downloads - A list of free files to download. Includes remote access client software.
- Contact Us - Mailing address, Email addresses and Support phone number.

Please feel free to ask any questions about the design. I will assist as much as possible.

Thank you for viewing. We promise to give constructive feedback to every person who submits a design. Thank you so much.

Target Market(s)

Restaurant and Cafe owners.

Industry/Entity Type

Hospitality

Requirements
Must have
• - Viewable on different resolutions and on smart phones and tablets.
- Clear call to action of EITHER 'Let's Meet For Coffee' or a "More information/Pricing" form to be completed by the visitor.

```html
<!DOCTYPE html>
<html lang="en">
<head>
<meta charset="utf-8">
<title>Falcon IT — Let's Meet For A Coffee</title>
<link rel="stylesheet" href="https://fonts.googleapis.com/css2?family=Arimo:ital,wght@0,400;0,700;1,400&family=Open+Sans:ital,wght@0,400;0,600;1,400&display=swap">
<style>
  :root {
    --brand-red: #b8232f;
    --brand-red-deep: #9c1a25;
    --charcoal: #2b2b2b;
    --charcoal-light: #3a3a3a;
    --field-grey: #dcdcdc;
    --panel-grey: #e1e1e1;
    --panel-border: #b9b9b9;
    --text-dark: #222;
    --text-mid: #555;
    --text-soft: #6a6a6a;
    --client-grey: #a8a8a8;
    --white: #fff;
  }
  * { box-sizing: border-box; margin: 0; padding: 0; }
  html, body { width: 895px; height: 1200px; overflow: hidden; }
  body {
    position: relative;
    background: var(--white);
    font-family: "Arimo", Arial, sans-serif;
    color: var(--text-dark);
  }
  .abs { position: absolute; }

  /* Header */
  .site-header {
    position: absolute; left: 0; top: 0; width: 895px; height: 51px;
    background: linear-gradient(#3a3a3a, #262626);
  }
  .brand { left: 32px; top: 9px; display: flex; align-items: center; gap: 8px; }
  .brand-dot { width: 30px; height: 30px; border-radius: 50%; background: var(--brand-red); }
  .brand-name { font-family: "Arimo", sans-serif; font-weight: 700; font-size: 26px; color: var(--white); }
  .main-nav { right: 36px; top: 21px; font-size: 13.5px; color: var(--white); }
  .main-nav a { color: var(--white); text-decoration: none; }
  .main-nav span { margin: 0 6px; }

  /* Hero */
  .hero {
    position: absolute; left: 0; top: 51px; width: 895px; height: 369px;
    background: radial-gradient(circle at 600px 200px, #c2303c 0%, var(--brand-red) 55%, #ad1f2b 100%);
  }
  .hero-rule { left: 13px; top: 365px; width: 870px; height: 4px; background: var(--brand-red-deep); }
  .field {
    position: absolute; left: 90px; width: 222px; height: 25px;
    background: var(--field-grey); border-radius: 4px;
    box-shadow: inset 0 3px 4px rgba(0,0,0,.35);
    font-family: "Open Sans", sans-serif; font-style: italic; font-size: 14px; color: #666;
    padding: 3px 0 0 24px;
  }
  .field-name { top: 70px; }
  .field-email { top: 108px; }
  .field-message { top: 146px; height: 139px; padding-top: 9px; }
  .btn-meet {
    left: 144px; top: 301px; width: 122px; height: 38px;
    background: linear-gradient(#444, #222); border-radius: 4px;
    color: var(--white); font-family: "Open Sans", sans-serif; font-size: 14.5px;
    text-align: center; line-height: 38px;
  }
  .hero-title {
    left: 455px; top: 40px; font-family: "Open Sans", sans-serif; font-style: italic;
    font-size: 31px; color: var(--white); text-shadow: 0 2px 3px rgba(0,0,0,.3);
  }
  .hero-visual {
    left: 447px; top: 117px; width: 334px; height: 222px; border-radius: 50% 50% 46% 46%;
    background: radial-gradient(ellipse at 50% 45%, #ffffff 0%, #ececec 55%, rgba(236,236,236,0) 72%);
  }

  /* Announcement */
  .notice {
    left: 13px; top: 433px; width: 870px; height: 68px;
    background: var(--panel-grey); border: 1px solid var(--panel-border);
  }
  .notice-title { left: 25px; top: 12px; font-size: 17px; color: var(--text-dark); }
  .notice-text { left: 25px; top: 38px; font-size: 13px; color: var(--text-mid); }
  .notice-icon { right: 35px; top: 12px; }

  /* Services */
  .service { position: absolute; top: 527px; width: 275px; }
  .service-icon { position: absolute; left: 0; top: 0; }
  .service-title { position: absolute; left: 51px; top: 1px; font-size: 17px; color: var(--brand-red); white-space: nowrap; }
  .service-sub { position: absolute; left: 51px; top: 21px; font-size: 13.5px; font-style: italic; color: var(--text-mid); }
  .service-body { position: absolute; left: 0; top: 46px; width: 275px; font-size: 11.5px; line-height: 16.8px; color: var(--text-dark); }
  .read-more { position: absolute; left: 96px; top: 142px; font-size: 12px; color: var(--brand-red); white-space: nowrap; }
  .read-more svg { margin-left: 6px; vertical-align: -1px; }

  /* Clients */
  .divider { left: 72px; top: 734px; width: 711px; height: 1px; background: linear-gradient(90deg, rgba(0,0,0,0), #555 30%, #555 70%, rgba(0,0,0,0)); }
  .clients-title { left: 0; top: 744px; width: 895px; text-align: center; font-size: 34px; color: var(--text-mid); }
  .client-row { left: 119px; top: 820px; width: 643px; display: flex; justify-content: space-between; align-items: center; }
  .client-name { font-family: "Arimo", sans-serif; font-size: 19px; color: var(--client-grey); }

  /* Testimonial */
  .testimonial {
    position: absolute; left: 0; top: 909px; width: 895px; height: 233px;
    background: radial-gradient(circle at 447px 120px, #c3404b 0%, var(--brand-red) 60%, #af202c 100%);
  }
  .testimonial-title { left: 0; top: 20px; width: 895px; text-align: center; font-size: 34px; color: var(--white); }
  .quote-mark { left: 108px; top: 78px; font-family: Georgia, serif; font-size: 70px; color: #7d1119; line-height: 1; }
  .quote-text { left: 175px; top: 95px; width: 590px; font-size: 13.5px; line-height: 17px; font-style: italic; color: var(--white); }
  .btn-works {
    left: 406px; top: 175px; width: 117px; height: 38px; border-radius: 4px;
    background: linear-gradient(#fafafa, #e4e4e4); color: var(--brand-red);
    font-size: 13.5px; text-align: center; line-height: 38px;
  }

  /* Footer */
  .site-footer { position: absolute; left: 0; top: 1142px; width: 895px; height: 58px; background: var(--charcoal); }
  .breadcrumb { left: 78px; top: 21px; font-size: 13px; color: #bbb; }
  .copyright { right: 24px; top: 20px; font-size: 13px; color: #ccc; }
</style>
</head>
<body>

<header class="site-header">
  <div class="abs brand"><span class="brand-dot"></span><span class="brand-name">Falcon IT</span></div>
  <nav class="abs main-nav">
    <a href="#">HOME</a><span>|</span><a href="#">Products</a><span>|</span><a href="#">Blog</a><span>|</span><a href="#">Pricing</a><span>|</span><a href="#">Contacts</a>
  </nav>
</header>

<section class="hero">
  <div class="field field-name">NAME</div>
  <div class="field field-email">Email</div>
  <div class="field field-message">Message</div>
  <div class="abs btn-meet">Let’s Meet</div>
  <h1 class="abs hero-title">Let’s Meet For A Coffee</h1>
  <div class="abs hero-visual" role="img" aria-label="Photo of a white coffee cup with a spoon on a saucer"></div>
  <div class="abs hero-rule"></div>
</section>

<section class="abs notice">
  <p class="abs notice-title">We are introducing something , Don’t miss it</p>
  <p class="abs notice-text">We are inroducing, Falcon Vault Service, Corvel Shieldware and Trelmo Suite for your business</p>
  <svg class="abs notice-icon" width="45" height="45" viewBox="0 0 45 45" aria-hidden="true">
    <circle cx="22.5" cy="22.5" r="22" fill="#3a3a3a"/>
    <circle cx="22.5" cy="12.5" r="3.2" fill="#fff"/>
    <path d="M18 19h7v13h3v3H17v-3h3V22h-2z" fill="#fff"/>
  </svg>
</section>

<article class="service" style="left:31px">
  <svg class="service-icon" width="41" height="41" viewBox="0 0 41 41" aria-hidden="true">
    <circle cx="20.5" cy="20.5" r="20" fill="var(--brand-red)"/>
    <path d="M10 19a11 11 0 0 1 19-6l2-2v7h-7l2.5-2.5A7.5 7.5 0 0 0 13.5 19z M31 22a11 11 0 0 1-19 6l-2 2v-7h7l-2.5 2.5A7.5 7.5 0 0 0 27.5 22z" fill="#fff"/>
  </svg>
  <h2 class="service-title">IT SUPPORT</h2>
  <p class="service-sub">Short Description</p>
  <p class="service-body">"Lorem ipsum dolor sit amet, consectetur adipisicing elit, sed do eiusmod tempor incididunt ut labore et dolore magna aliqua. Ut enim ad minim veniam, quis nostrud exercitation ullamco laboris nisi ut aliquip ex ea commodo consequat.</p>
  <a class="read-more">Read More<svg width="6" height="10" viewBox="0 0 6 10"><path d="M0.5 0.5l5 4.5-5 4.5z" fill="none" stroke="#999"/></svg></a>
</article>

<article class="service" style="left:314px">
  <svg class="service-icon" width="41" height="41" viewBox="0 0 41 41" aria-hidden="true">
    <circle cx="20.5" cy="20.5" r="20" fill="var(--brand-red)"/>
    <path d="M12 27a5 5 0 0 1 0-10a7 7 0 0 1 13-2a6 6 0 0 1 5 12z" fill="#fff"/>
  </svg>
  <h2 class="service-title">Falcon Vault</h2>
  <p class="service-sub">Short Description</p>
  <p class="service-body">"Lorem ipsum dolor sit amet, consectetur adipisicing elit, sed do eiusmod tempor incididunt ut labore et dolore magna aliqua. Ut enim ad minim veniam, quis nostrud exercitation ullamco laboris nisi ut aliquip ex ea commodo consequat.</p>
  <a class="read-more">Read More<svg width="6" height="10" viewBox="0 0 6 10"><path d="M0.5 0.5l5 4.5-5 4.5z" fill="none" stroke="#999"/></svg></a>
</article>

<article class="service" style="left:599px; top:530px">
  <svg class="service-icon" width="41" height="41" viewBox="0 0 41 41" aria-hidden="true">
    <circle cx="20.5" cy="20.5" r="20" fill="var(--brand-red)"/>
    <path d="M10 28l10-10 3 3-10 10z" fill="#fff"/>
    <path d="M26 12v8M22 16h8" stroke="#fff" stroke-width="2.4"/>
  </svg>
  <h2 class="service-title">Antivirus &amp; Apps</h2>
  <p class="service-sub">Short Description</p>
  <p class="service-body">"Lorem ipsum dolor sit amet, consectetur adipisicing elit, sed do eiusmod tempor incididunt ut labore et dolore magna aliqua. Ut enim ad minim veniam, quis nostrud exercitation ullamco laboris nisi ut aliquip ex ea commodo consequat.</p>
  <a class="read-more">Read More<svg width="6" height="10" viewBox="0 0 6 10"><path d="M0.5 0.5l5 4.5-5 4.5z" fill="none" stroke="#999"/></svg></a>
</article>

<div class="abs divider"></div>
<h2 class="abs clients-title">Our Awesome Clients</h2>
<div class="abs client-row">
  <span class="client-name">Harlow Stays</span>
  <span class="client-name">Meridel Hotels</span>
  <span class="client-name">Harlow Stays</span>
  <span class="client-name">Meridel Hotels</span>
  <span class="client-name">Harlow Stays</span>
</div>

<section class="testimonial">
  <h2 class="abs testimonial-title">People Love Us</h2>
  <div class="abs quote-mark">“</div>
  <p class="abs quote-text">Lorem Ipsum is simply dummy text of the printing and typesetting industry. Lorem Ipsum has been the industry's standard dummy text ever since the 1500s, when an unknown printer took a galley of type and scrambled it</p>
  <div class="abs btn-works">See Our Works</div>
</section>

<footer class="site-footer">
  <p class="abs breadcrumb">Home /&nbsp; Products / etc</p>
  <p class="abs copyright">Copyright 2012 INC. All rights reserved.</p>
</footer>

</body>
</html>
```